Flyer to Promote Membership in a Trade Association

UPDATE: I am looking for something modern and clean. NO CLIP ART. Not flashy. Just professional and modern. For everyone looking at our current flyer, we don't like it. That's why we aer looking for a new one. So please don't replicate it or use it as inspiration.

I need a flyer to promote membership in the Durable Residence Backers League. It can (probably should) be 2-sided. The content is attached as well as our logo and brand guidelines.

```html
<!DOCTYPE html>
<html lang="en">
<head>
<meta charset="utf-8">
<title>Durable Residence Backers League – Membership Flyer</title>
<link rel="stylesheet" href="https://fonts.googleapis.com/css2?family=Oswald:wght@500;600&family=Source+Sans+3:wght@400;600;700;800&display=swap">
<style>
:root{
  --stage:#8b8b8b;
  --paper:#ffffff;
  --orange:#f08a2c;
  --orange-deep:#e06f12;
  --brown:#2c1d0f;
  --ink:#1f1f1f;
  --muted:#5a5a5a;
  --line:#cfcfcf;
  --tile-line:#d9d9d9;
  --cream:#fff6ec;
}
*{box-sizing:border-box;margin:0;padding:0}
html,body{width:1200px;height:1061px;overflow:hidden}
body{background:var(--stage);font-family:"Source Sans 3",Arial,sans-serif;color:var(--ink);position:relative}
.page{position:absolute;width:435px;height:564px;background:var(--paper);overflow:hidden;box-shadow:0 4px 14px rgba(0,0,0,.25)}
.page--front{left:115px;top:236px}
.page--back{left:644px;top:233px}
.abs{position:absolute}

/* brand mark */
.brand{display:flex;align-items:center;gap:6px;font-family:"Source Sans 3",sans-serif;font-weight:800;color:var(--orange-deep);font-size:25px;letter-spacing:.5px}
.brand__square{width:20px;height:20px;background:var(--orange-deep)}

/* front hero */
.hero-band{left:0;top:73px;width:262px;height:172px;background:linear-gradient(180deg,var(--orange) 0%,var(--orange-deep) 60%,#a8521a 100%)}
.hero-title{left:24px;top:84px;color:#fff;font-family:"Oswald",sans-serif;line-height:1}
.hero-title__small{font-size:20px;font-weight:500;letter-spacing:1px}
.hero-title__big{font-size:33px;font-weight:600;margin-top:4px;line-height:1.02}
.hero-photo{left:190px;top:42px;width:230px;height:248px;clip-path:polygon(25% 2%,75% 2%,100% 50%,75% 98%,25% 98%,0 50%);background:linear-gradient(160deg,#cfc6bd,#8d7f74 55%,#4a3f39)}
.headline{left:18px;top:255px;width:240px;font-size:18px;font-weight:700;line-height:1.08}
.subhead{left:18px;top:299px;font-size:13px;font-weight:600;line-height:1.2}
.subhead span{color:var(--orange-deep);font-weight:700;display:block}
.intro{left:18px;top:335px;width:225px;font-size:6.6px;line-height:1.35;color:var(--muted)}
.stats{left:236px;top:305px;width:190px;font-family:"Oswald",sans-serif;color:var(--orange-deep)}
.stat{display:inline-flex;align-items:flex-end;gap:3px;margin-right:8px}
.stat__num{font-size:22px;font-weight:600;line-height:1}
.stat__label{font-size:9px;line-height:1;color:var(--ink);text-transform:uppercase;font-weight:600}
.stat__label em{color:var(--orange-deep);font-style:normal;display:block}
.stat--wide .stat__num{font-size:28px}

.does-tab{left:0;top:382px;width:118px;height:15px;background:var(--orange-deep);color:#fff;font-size:8.5px;font-weight:700;padding:2px 0 0 18px}
.does-list{left:10px;top:402px;list-style:none;font-size:6.2px;color:var(--muted);line-height:1.15}
.does-list li{display:flex;gap:6px;margin-bottom:3.4px}
.does-list i{width:9px;height:9px;background:var(--orange);border-radius:2px;margin-top:1px;flex:none}
.does-list b{display:block;color:var(--ink);font-size:6.8px}
.person-photo{left:112px;top:396px;width:58px;height:108px;background:linear-gradient(180deg,#d9d2cb,#9b8d80 70%,#6b5d52)}

.access{left:145px;top:382px;width:290px;height:45px;background:var(--brown);color:#fff;text-align:center;padding-top:3px}
.access__title{color:var(--orange);font-size:11px;font-weight:700}
.access__sub{font-size:8.5px}
.access__btn{display:inline-block;margin-top:2px;background:var(--orange-deep);color:#fff;font-size:8px;font-weight:700;padding:1px 9px;border-radius:2px}
.tier{left:170px;width:265px;height:36px;display:flex;justify-content:space-between;align-items:center;padding:0 14px 0 12px}
.tier--investor{top:430px;background:var(--cream)}
.tier--affiliate{top:470px;height:30px;background:var(--orange-deep);color:#fff}
.tier__name{font-size:11px;font-weight:700;color:var(--orange-deep);line-height:1}
.tier--affiliate .tier__name{color:#fff}
.tier__who{display:block;font-size:6.5px;font-weight:600;color:var(--ink);margin-top:2px;text-align:center}
.tier--affiliate .tier__who{color:#fff}
.tier__price{font-size:8px;font-weight:700;line-height:1.35}
.tier__price small{font-size:5.5px;font-weight:400}

.footer{left:0;bottom:0;width:435px;height:56px;background:var(--brown)}
.footer__tab{position:absolute;left:96px;top:0;width:245px;height:27px;background:var(--orange-deep);border-radius:0 0 16px 16px;color:#fff;font-size:13px;font-weight:700;display:flex;align-items:center;justify-content:center;gap:8px}
.footer__tab svg{width:12px;height:12px}

/* back */
.benefits-tab{left:0;top:22px;width:214px;height:33px;background:var(--orange-deep);clip-path:polygon(0 0,88% 0,100% 100%,0 100%);color:#fff;font-size:17px;font-weight:700;padding:5px 0 0 22px}
.benefits-tab::after{content:"";position:absolute}
.back-brand{right:20px;top:22px}
.benefit{width:178px;border:1px solid var(--line);border-radius:5px;padding:0 6px 4px 8px;background:#fff}
.benefit__title{display:flex;align-items:center;gap:4px;font-size:8px;font-weight:700;color:var(--orange-deep);line-height:1.05;margin-top:-6px;background:#fff;width:max-content;padding-right:3px}
.benefit__title i{width:10px;height:10px;background:#555;flex:none}
.benefit__text{font-size:5.8px;line-height:1.35;color:var(--muted);margin-top:3px}
.members-title{left:0;top:318px;width:435px;text-align:center;font-size:17px;font-weight:700;color:var(--orange-deep)}
.logo-grid{left:22px;top:343px;width:392px;display:grid;grid-template-columns:repeat(7,1fr);gap:0}
.logo-grid--last{left:50px;top:463px;width:336px;grid-template-columns:repeat(6,1fr)}
.logo-tile{height:38px;border:1px solid var(--tile-line);margin:0 0 2px -1px;display:flex;align-items:center;justify-content:center;text-align:center;font-size:6.4px;font-weight:700;color:#2d3a66;padding:0 2px;line-height:1.05}
</style>
</head>
<body>

<!-- FRONT -->
<section class="page page--front">
  <div class="abs brand" style="left:22px;top:20px"><span class="brand__square"></span>DRBL</div>

  <div class="abs hero-band" role="img" aria-label="Warm orange-toned photograph of a city skyline at sunset"></div>
  <h1 class="abs hero-title">
    <div class="hero-title__small">DURABLE</div>
    <div class="hero-title__big">RESIDENCE<br>BACKERS<br>LEAGUE</div>
  </h1>
  <div class="abs hero-photo" role="img" aria-label="Photograph of members talking at a conference table"></div>

  <h2 class="abs headline">Where LIHTC Investing Excellence Begins</h2>
  <p class="abs subhead">The Only Community<span>Built Exclusively for Investors</span></p>
  <p class="abs intro">DRBL is where federal housing credit investors connect, learn, and lead. We are the only organization solely dedicated to LIHTC investors, giving you a trusted peer network, industry-setting standards, and the insights to stay informed.</p>

  <div class="abs stats">
    <div class="stat"><span class="stat__num">30</span><span class="stat__label">Years<em>of impact</em></span></div>
    <div class="stat"><span class="stat__num">+60</span><span class="stat__label">Investor<em>firms</em></span></div>
    <div class="stat stat--wide" style="margin-top:4px"><span class="stat__num">+1000</span><span class="stat__label">Industry<em>professionals</em></span></div>
  </div>

  <div class="abs does-tab">What Members Do</div>
  <ul class="abs does-list">
    <li><i></i><span><b>Network</b>Peer Groups &amp; Forums</span></li>
    <li><i></i><span><b>Learn</b>Conferences &amp; Webinars</span></li>
    <li><i></i><span><b>Share</b>Candid Investor Exchange</span></li>
    <li><i></i><span><b>Shape</b>Standards &amp; Best Practices</span></li>
    <li><i></i><span><b>Grow</b>Professional Development</span></li>
  </ul>
  <div class="abs person-photo" role="img" aria-label="Photograph of a speaker presenting at an event"></div>

  <div class="abs access">
    <div class="access__title">One membership, unlimited access.</div>
    <div class="access__sub">Your entire team can participate in DRBL activities.</div>
    <span class="access__btn">Join DRBL Today</span>
  </div>
  <div class="abs tier tier--investor">
    <div><div class="tier__name">Investor Members</div><span class="tier__who">Banks, Insurance Companies,<br>Economic Investors</span></div>
    <div class="tier__price">⊙ 5,000$ <small>/year (assets US$B)</small><br>⊙ 1,000$ <small>/year (assets US$B)</small></div>
  </div>
  <div class="abs tier tier--affiliate">
    <div><div class="tier__name">Affiliate Members</div><span class="tier__who">Syndicators &amp; Brokers</span></div>
    <div class="tier__price">⊙ 4,500$ <small>/year</small></div>
  </div>

  <footer class="abs footer">
    <div class="footer__tab">Ready to join?
      <svg viewBox="0 0 12 12"><circle cx="6" cy="6" r="5" fill="none" stroke="#fff" stroke-width="1.2"/><ellipse cx="6" cy="6" rx="2.2" ry="5" fill="none" stroke="#fff" stroke-width="1"/><line x1="1" y1="6" x2="11" y2="6" stroke="#fff"/></svg>
      www.drbl.org</div>
  </footer>
</section>

<!-- BACK -->
<section class="page page--back">
  <div class="abs benefits-tab">Member Benefits</div>
  <div class="abs brand back-brand"><span class="brand__square"></span>DRBL</div>

  <article class="abs benefit" style="left:28px;top:74px">
    <h3 class="benefit__title"><i></i>Emerging Leaders Program<br>[INVESTOR ONLY]</h3>
    <p class="benefit__text">Develop your firm's next-generation leaders through dedicated professional development programming.</p>
  </article>
  <article class="abs benefit" style="left:28px;top:131px">
    <h3 class="benefit__title"><i></i>Investor-Only Forums</h3>
    <p class="benefit__text">Exclusive meetings and webinars for investors only, enabling candid conversations and meaningful collaboration.</p>
  </article>
  <article class="abs benefit" style="left:28px;top:189px">
    <h3 class="benefit__title"><i></i>Peer-to-Peer Meetups</h3>
    <p class="benefit__text">Find your peers—underwriters, asset managers, credit officers and more—with our meetups.</p>
  </article>
  <article class="abs benefit" style="left:28px;top:239px">
    <h3 class="benefit__title"><i></i>Live &amp; On-Demand Webinars</h3>
    <p class="benefit__text">Free monthly Third Thursday webinars covering Year 15 issues, secondary transactions, securitizing developer fees and other emerging topics.</p>
  </article>

  <article class="abs benefit" style="left:219px;top:78px">
    <h3 class="benefit__title"><i></i>Members-Only Conferences</h3>
    <p class="benefit__text">Two annual in-person meetings. Spring Meeting: investors-only for candid peer conversations. Fall Summit: full ecosystem gathering with syndicators and brokers.</p>
  </article>
  <article class="abs benefit" style="left:219px;top:151px">
    <h3 class="benefit__title"><i></i>Searchable Member Directory</h3>
    <p class="benefit__text">Find underwriters, asset managers, and credit officers—searchable by role, firm type, and investment approach.</p>
  </article>
  <article class="abs benefit" style="left:219px;top:222px">
    <h3 class="benefit__title"><i></i>Shape Industry Standards<br>[INVESTOR ONLY]</h3>
    <p class="benefit__text">DRBL's underwriting and asset management standards are adopted industry-wide. Influence them through our committees.</p>
  </article>

  <h2 class="abs members-title">Our Investor Members Include</h2>
  <div class="abs logo-grid">
    <div class="logo-tile">Kestrel Mutual</div>
    <div class="logo-tile">Brindle</div>
    <div class="logo-tile">Meridian Charge</div>
    <div class="logo-tile">Harbor Union Bank</div>
    <div class="logo-tile">Ridgeway</div>
    <div class="logo-tile">Oakline Financial</div>
    <div class="logo-tile">Summit Crest</div>
    <div class="logo-tile">Calder Trust</div>
    <div class="logo-tile">Norland</div>
    <div class="logo-tile">Civic Home Fund</div>
    <div class="logo-tile">Fairmont Bank</div>
    <div class="logo-tile">Granger Hale</div>
    <div class="logo-tile">Lantern Bank</div>
    <div class="logo-tile">Whitby Stone</div>
    <div class="logo-tile">Pinefield</div>
    <div class="logo-tile">Eastgate Life</div>
    <div class="logo-tile">Corvane</div>
    <div class="logo-tile">Tallis Real Estate</div>
    <div class="logo-tile">Bayridge</div>
    <div class="logo-tile">Solmara</div>
    <div class="logo-tile">Kirin Coast</div>
  </div>
  <div class="abs logo-grid logo-grid--last">
    <div class="logo-tile">Vale Bank</div>
    <div class="logo-tile">Hearth Bank</div>
    <div class="logo-tile">Alder Capital</div>
    <div class="logo-tile">Norvik</div>
    <div class="logo-tile">Patriot Mutual</div>
    <div class="logo-tile">Westbrook</div>
  </div>

  <footer class="abs footer">
    <div class="footer__tab">Ready to join?
      <svg viewBox="0 0 12 12"><circle cx="6" cy="6" r="5" fill="none" stroke="#fff" stroke-width="1.2"/><ellipse cx="6" cy="6" rx="2.2" ry="5" fill="none" stroke="#fff" stroke-width="1"/><line x1="1" y1="6" x2="11" y2="6" stroke="#fff"/></svg>
      www.drbl.org</div>
  </footer>
</section>

</body>
</html>
```